Verdant Loop Advisors, LLC

I am looking for a simple, clear layout with my logo prominent and embossed, on the best quality card stock available. I would like the business name and phone number included on the card as well......I dont want my name anywhere on the card and I would like my logo embossed on the card......something simple with a white back......open to designs as long as they go along with recycling symbols and green type stuff.....The address, website, cell number, fax number, and email are listed below

5374 Tillbury Fenwood Road
Hyattsville, MD 20785

c. 555.555.0143 f. 240.555.0187
e. sales@verdantloopadvisors.example
w. www.verdantloopadvisors.example

Industry/Entity Type

Recycling

```html
<!DOCTYPE html>
<html lang="en">
<head>
<meta charset="utf-8">
<title>Verdant Loop Advisors, LLC – Business Card</title>
<link rel="stylesheet" href="https://fonts.googleapis.com/css2?family=Michroma&family=Saira:wght@500;600&display=swap">
<style>
  :root {
    --backdrop: #e9ece6;
    --card-white: #ffffff;
    --sky-band: #8ec5f8;
    --sky-stripe: #c3e0fb;
    --mint-band: #b2f5aa;
    --ink: #111111;
    --brand-ink: #2b2a1f;
    --brand-green: #1e7a3a;
    --globe-blue: #b9c8e8;
    --leaf-green: #d9efc9;
  }
  html, body {
    margin: 0;
    padding: 0;
    width: 1200px;
    height: 686px;
    overflow: hidden;
    background: var(--backdrop);
  }
  .card {
    position: absolute;
    left: 34px;
    top: 27px;
    width: 990px;
    height: 552px;
    background: var(--card-white);
    transform: scale(1.1429);
    transform-origin: top left;
    overflow: hidden;
  }
  .header-band {
    position: absolute;
    left: 0; top: 0;
    width: 990px; height: 104px;
    background: linear-gradient(to bottom,
      var(--sky-band) 0, var(--sky-band) 33px,
      var(--sky-stripe) 33px, var(--sky-stripe) 62px,
      var(--sky-band) 62px, var(--sky-band) 104px);
  }
  .brand {
    position: absolute;
    left: 0; top: 0;
    width: 990px; height: 104px;
    display: flex;
    align-items: center;
    justify-content: center;
    gap: 16px;
  }
  .brand-dot {
    width: 58px; height: 58px;
    border-radius: 50%;
    background: var(--brand-green);
  }
  .brand-name {
    display: flex;
    flex-direction: column;
    font-family: "Saira", sans-serif;
    font-weight: 600;
    color: var(--brand-ink);
    text-transform: uppercase;
  }
  .brand-name-main {
    font-size: 40px;
    line-height: 38px;
    letter-spacing: 2px;
  }
  .brand-name-sub {
    font-size: 15px;
    line-height: 18px;
    letter-spacing: 11.5px;
  }
  .earth-leaf-art {
    position: absolute;
    left: 540px; top: 104px;
    width: 450px; height: 390px;
    background:
      radial-gradient(circle 175px at 180px 142px, var(--globe-blue) 0, rgba(185,200,232,0.75) 80%, rgba(255,255,255,0) 100%),
      radial-gradient(ellipse 260px 170px at 300px 270px, var(--leaf-green) 0, rgba(217,239,201,0.5) 60%, rgba(255,255,255,0) 100%);
  }
  .contact {
    position: absolute;
    left: 32px;
    top: 206px;
    font-family: "Saira", sans-serif;
    font-weight: 500;
    color: var(--ink);
  }
  .contact p { margin: 0; }
  .address { font-size: 27px; line-height: 36px; }
  .phone { font-size: 27px; line-height: 36px; margin-top: 33px !important; }
  .online { font-size: 23px; line-height: 35px; }
  .footer-band {
    position: absolute;
    left: 0; top: 494px;
    width: 990px; height: 58px;
    background: var(--mint-band);
  }
  .footer-name {
    position: absolute;
    right: 20px;
    top: 18px;
    margin: 0;
    font-family: "Michroma", sans-serif;
    font-size: 16px;
    letter-spacing: 1px;
    color: var(--ink);
  }
</style>
</head>
<body>
  <div class="card">
    <div class="header-band"></div>
    <div class="brand">
      <span class="brand-dot"></span>
      <span class="brand-name">
        <span class="brand-name-main">Verdant Loop</span>
        <span class="brand-name-sub">Advisors LLC</span>
      </span>
    </div>

    <div class="earth-leaf-art" role="img" aria-label="Faded photo of planet Earth resting on a green leaf"></div>

    <div class="contact">
      <p class="address">5374 Tillbury Fenwood Road<br>Glenmarsh,ZZ 00785</p>
      <p class="phone">555.555.0143</p>
      <p class="online">sales@verdantloopadvisors.example<br>www.verdantloopadvisors.example</p>
    </div>

    <div class="footer-band">
      <p class="footer-name">VERDANT LOOP ADVISORS</p>
    </div>
  </div>
</body>
</html>
```